Carpentry company Needs a business card design

We need a design for a Carpentry / building company, business card. Please think of designs out of the ordinary and try to make it eye catching. Our existing logo will need to be incorporated in the design. However feel free to change the colours of the logo to suit your design. I would like to see some designs with green /black and orange incorporated into it.These are not the only colours accepted and all designs that appeal will be accepted.

Please contact me should you have any questions
Thanks Marcus

Target Market(s)

General Public seeking carpentry work

Industry/Entity Type

Business

Contact Information for Business Card

- Current company logo ( colours can be changed)
-Phone number ,
- info@brantelworks.com.au
- brantelworks.com.au
-the facebook symbol

Font styles to use
Other font styles liked:
• You choose

Requirements
Must have
• Services we provide
• - Renovations
• -Deckings & Pergolas
• -Kitchens
• - Bathrooms
• - Intricate details
Nice to have
• an awesome design
Should not have
• Tools on the business card

```html
<!DOCTYPE html>
<html lang="en">
<head>
<meta charset="utf-8">
<title>Brantel Works – Business Card</title>
<link href="https://fonts.googleapis.com/css2?family=Anton&family=Raleway:wght@400;800&display=swap" rel="stylesheet">
<style>
  :root{
    --page:#e4e4e2;
    --card-black:#120b0c;
    --green-deep:#00a54f;
    --green-brand:#22b24c;
    --green-light:#8cc866;
    --green-text:#93d872;
    --white:#ffffff;
  }
  *{margin:0;padding:0;box-sizing:border-box}
  html,body{width:1200px;height:900px;overflow:hidden;background:var(--page)}
  .sheet{position:relative;width:1200px;height:900px}
  .card{position:absolute;left:250px;width:700px;height:390px;background:var(--card-black);overflow:hidden;box-shadow:0 6px 18px rgba(0,0,0,.25)}
  .card--front{top:40px}
  .card--back{top:470px}

  .brand{position:absolute;top:62px;left:0;width:100%;display:flex;justify-content:center;align-items:center;gap:18px}
  .brand__mark{width:34px;height:34px;background:var(--green-brand)}
  .brand__name{font-family:"Raleway",sans-serif;font-weight:800;font-size:58px;letter-spacing:2px;color:var(--green-brand);line-height:1}
  .brand__rule{position:absolute;top:152px;left:120px;width:460px;height:6px;background:var(--green-brand)}

  .contacts{position:absolute;top:200px;left:200px;list-style:none;font-family:"Raleway",sans-serif;font-size:21px;color:var(--green-text)}
  .contacts li{display:flex;align-items:center;gap:16px;height:34px}
  .contacts svg{width:26px;height:26px;flex:none}

  .services{position:absolute;inset:0;width:700px;height:390px}
  .services text{font-family:"Anton",sans-serif}
  .services__title{font-size:40px;fill:var(--white)}
  .services__item{font-size:34px}
  .on-light{fill:var(--card-black)}
  .on-dark{fill:var(--green-light)}
</style>
</head>
<body>
<main class="sheet">

  <section class="card card--front" aria-label="Card front">
    <div class="brand">
      <span class="brand__mark"></span>
      <span class="brand__name">BRANTEL WORKS</span>
    </div>
    <div class="brand__rule"></div>

    <ul class="contacts">
      <li>
        <svg viewBox="0 0 26 26" aria-hidden="true"><circle cx="13" cy="13" r="12" fill="var(--green-light)"/><path d="M9 7l2.5 0 1 3-1.6 1.2a8 8 0 0 0 3.9 3.9L16 13.5l3 1v2.5c0 .8-.7 1.5-1.5 1.4A11 11 0 0 1 7.6 8.5C7.5 7.7 8.2 7 9 7z" fill="var(--card-black)"/></svg>
        <span>0400 555 018</span>
      </li>
      <li>
        <svg viewBox="0 0 26 26" aria-hidden="true"><circle cx="13" cy="13" r="12" fill="var(--green-light)"/><rect x="7" y="8.5" width="12" height="9" fill="none" stroke="var(--card-black)" stroke-width="1.6"/><path d="M7 8.5l6 5 6-5" fill="none" stroke="var(--card-black)" stroke-width="1.6"/></svg>
        <span>info@brantelworks.com.au</span>
      </li>
      <li>
        <svg viewBox="0 0 26 26" aria-hidden="true"><rect x="2" y="2" width="22" height="22" fill="var(--green-light)"/></svg>
        <span>brantelworks.com.au</span>
      </li>
    </ul>
  </section>

  <section class="card card--back" aria-label="Card back: services">
    <svg class="services" viewBox="0 0 700 390">
      <defs>
        <linearGradient id="feature-fill" x1="0" y1="0" x2="1" y2="0">
          <stop offset="0" stop-color="var(--green-light)"/>
          <stop offset="1" stop-color="var(--green-deep)"/>
        </linearGradient>
      </defs>

      <rect class="band" x="0" y="105" width="700" height="45" fill="var(--green-light)"/>
      <rect class="band" x="0" y="195" width="700" height="50" fill="var(--green-light)"/>
      <rect class="band" x="0" y="290" width="700" height="50" fill="var(--green-light)"/>

      <rect class="feature" x="0" y="0" width="260" height="390" fill="url(#feature-fill)" role="img" aria-label="Decorative green arrow graphic"/>

      <text class="services__title" x="302" y="66">Services we provide</text>
      <text class="services__item on-light" x="340" y="141">Renovations</text>
      <text class="services__item on-dark" x="340" y="186">Deckings &amp; Pergolas</text>
      <text class="services__item on-light" x="340" y="234">Kitchens</text>
      <text class="services__item on-dark" x="340" y="281">Bathrooms</text>
      <text class="services__item on-light" x="340" y="329">Intricate details</text>
    </svg>
  </section>

</main>
</body>
</html>
```